HairDressing and Beauty Salon Website

**Any private solicitations sent outside this platform will be ignored**

I need a website design for my luxury hair dressing and beauty salon.

The style to follow for this website can should match the following designs;
www.qerntavo.com.au
www.dumisker.com.au

The design should incorporate a prominent "Book Appointment" button.

The design should incorporate a "Buy Gift Certificate" button.

The main page should provide a reviews section where I can display customer reviews.

Colors
Main colors are white and black with purple / teal color highlights.

I need 5 pages designed;
About -> See archive with about text. Should have a top header image as shown in the websites above
Services -> List various services offered included in the Services folder of the attached archive
Shopping -> A grid of hair style related products for sale
Photos -> Photos are provided in the Photos folder in the attached archive
Contact -> Include a google map, address, book appointment button

Target Market(s)

High end luxury beauty and hair salon

Industry/Entity Type

Hair And Beauty

Number of Pages Required

5+ page

Colors
876aae
86cfc6
ffffff

Requirements
Must have
• - Book appointment button
- Social media buttons + Orchard Appshelf + Brindle App Market buttons to download mobile app associated with website

```html
<!DOCTYPE html>
<html lang="en">
<head>
<meta charset="utf-8">
<title>Lumera Solenne — Hair &amp; Beauty Salon</title>
<link href="https://fonts.googleapis.com/css2?family=Cormorant+Garamond:wght@400;500&family=Montserrat:wght@400;500;600&display=swap" rel="stylesheet">
<style>
:root{
  --purple:#876aae;
  --teal:#86cfc6;
  --white:#ffffff;
  --ink:#111111;
  --dark:#2b2d2b;
  --grey:#555555;
  --lavender:#ecebf3;
}
*{box-sizing:border-box;margin:0;padding:0}
html,body{width:1200px;height:4421px;overflow:hidden}
body{position:relative;background:var(--white);font-family:'Montserrat',sans-serif;color:var(--ink)}
.abs{position:absolute}
.serif{font-family:'Cormorant Garamond',serif}
.btn{position:absolute;display:flex;align-items:center;justify-content:center;font-size:14px;letter-spacing:.5px;text-transform:uppercase;text-decoration:none}
.btn-solid{background:var(--purple);color:var(--white)}
.btn-line{border:1.5px solid var(--purple);color:var(--white)}
.btn-ghost{border:1.5px solid #333;color:#222;font-size:13px}

/* header */
.site-header{top:0;left:0;width:1200px;height:82px;background:var(--white)}
.brand{left:108px;top:20px;line-height:1}
.brand-top{font-size:17px;letter-spacing:1px}
.brand-sub{font-size:9px;margin-top:8px;letter-spacing:.5px}
.main-nav{right:102px;top:34px;display:flex;gap:42px;font-family:'Cormorant Garamond',serif;font-size:13px;letter-spacing:1px}

/* hero */
.hero{top:82px;left:0;width:1200px;height:571px;
  background:
    radial-gradient(ellipse 30% 40% at 50% 55%,rgba(255,255,255,.9),rgba(255,255,255,0)),
    linear-gradient(180deg,rgba(0,0,0,.35) 0%,rgba(0,0,0,0) 20%,rgba(0,0,0,0) 85%,rgba(60,70,55,.35) 100%),
    linear-gradient(90deg,#1a1c1b 0%,#2f3a2c 7%,#3a3c3b 11%,#dfe2e8 16%,#f2f2f5 40%,#e8e8ee 60%,#b9b8c2 80%,#4a4c4a 92%,#2c3a29 96%,#1a1c1b 100%)}

/* about */
.about{top:653px;left:0;width:1200px;height:384px;background:
  linear-gradient(90deg,#e4e2ee 0%,#ecebf3 18%,#e2dfec 33%,#f1f0f6 50%,#e2dfec 67%,#ecebf3 82%,#e4e2ee 100%)}
.about h2{position:absolute;top:40px;width:100%;text-align:center;font-family:'Cormorant Garamond',serif;font-weight:400;font-size:58px;letter-spacing:1px}
.about p{position:absolute;width:100%;text-align:center;font-size:14.5px;line-height:18px}

/* services */
.services{top:1037px;left:0;width:1200px;height:602px;background:var(--dark)}
.section-title{font-family:'Cormorant Garamond',serif;font-weight:400;color:var(--purple);font-size:58px;letter-spacing:1px}
.service-list{left:102px;top:133px;color:var(--white);font-size:19.5px;letter-spacing:.5px}
.service-list li{list-style:none;height:49px}
.service-list .sep{color:var(--purple);margin:0 28px}

/* products */
.product{position:absolute;top:1791px;width:167px}
.product-shot{width:167px;height:256px;background:linear-gradient(180deg,#ffffff 0%,#ffffff 18%,#8a6fb3 18%,#7e63a8 100%)}
.product-name{margin-top:14px;font-size:14px;color:#333}
.product-price{margin-top:10px;font-size:14px;color:#333}

/* gallery */
.dot{position:absolute;top:2824px;width:42px;height:4px;background:#d3d3d3}

/* testimonial */
.testimonial{top:2921px;left:0;width:1200px;height:437px;background:var(--dark);color:var(--white)}

/* gift */
.gift{top:3358px;left:0;width:1200px;height:396px;background:var(--white)}

/* find us */
.find{top:3754px;left:0;width:1200px;height:438px;background:var(--dark);color:var(--white)}
.find .row{position:absolute;left:102px;font-size:14px;display:flex;align-items:center;gap:6px}

/* footer */
.site-footer{top:4192px;left:0;width:1200px;height:229px;background:var(--white)}
.social{position:absolute;top:86px;left:150px;width:200px;display:flex;justify-content:center;gap:18px;font-size:12px}
.social span{display:flex;align-items:center;gap:6px}
.social i{display:block;width:14px;height:14px;background:var(--purple)}
.footer-nav{position:absolute;top:165px;width:100%;display:flex;justify-content:center;gap:26px;font-size:11.5px}
.app-badge{position:absolute;left:897px;width:82px;height:24px;background:#111;color:var(--white);border-radius:4px;font-size:7.5px;display:flex;align-items:center;justify-content:center}
</style>
</head>
<body>

<header class="abs site-header">
  <div class="abs brand">
    <div class="brand-top">Velmora</div>
    <div class="brand-sub">by Lumera Solenne</div>
  </div>
  <nav class="abs main-nav"><span>ABOUT</span><span>SERVICES</span><span>SHOPPING</span><span>PHOTOS</span><span>CONTACT</span></nav>
</header>

<section class="abs hero" role="img" aria-label="Photograph of the salon storefront with product displays, styling stations and potted trees either side">
  <a class="btn btn-solid" style="left:475px;top:424px;width:248px;height:58px">Book Appointment</a>
</section>

<section class="abs about">
  <h2>ABOUT US</h2>
  <p style="top:143px">Lumera Solenne is a boutique hair and beauty salon operating in the lovely harbourside suburb of Tidewater Bay.</p>
  <p style="top:180px">The salon is a family business that prides itself on its close team of hair and beauty professionals that provide a<br>fantastic environment for its clients and friends to enjoy an amazing lux experience.</p>
  <a class="btn btn-solid" style="left:475px;top:259px;width:248px;height:58px">Learn More</a>
</section>

<section class="abs services">
  <h2 class="abs section-title" style="left:102px;top:26px">OUR SERVICES</h2>
  <ul class="abs service-list">
    <li>BALAYAGE<span class="sep">|</span>MAKE-UP</li>
    <li>WAXING<span class="sep">|</span>NAILS<span class="sep">|</span>BLOWDRY</li>
    <li>UP STYLE<span class="sep">|</span>BRAIDING</li>
    <li>VELMORA HAIR CARE RITUALS</li>
    <li>HAIR EXTENSIONS<span class="sep">|</span>CUTTING</li>
    <li>FORM AND SMOOTH</li>
    <li>HIGHLIGHTS<span class="sep">|</span>TINT</li>
  </ul>
  <a class="btn btn-line" style="left:102px;top:500px;width:249px;height:58px">View All Services</a>
  <div class="abs" role="img" aria-label="Photograph of long wavy ash-brown hair seen from behind" style="left:678px;top:41px;width:458px;height:514px;background:radial-gradient(ellipse 60% 55% at 55% 60%,#a8979a,rgba(120,105,108,0) 70%),linear-gradient(180deg,#303039 0%,#5a5055 25%,#8c7c7c 60%,#6b5f62 100%)"></div>
</section>

<h2 class="abs section-title" style="left:102px;top:1672px">OUR PRODUCTS</h2>
<a class="btn btn-ghost" style="left:847px;top:1675px;width:250px;height:58px;border-color:var(--purple)">Shop All Products</a>

<div class="product" style="left:122px"><div class="product-shot" role="img" aria-label="Hair conditioner bottle on purple backdrop"></div><div class="product-name">Hair Conditioner</div><div class="product-price">$50</div><a class="btn btn-ghost" style="position:relative;margin-top:16px;width:167px;height:40px">Add to Cart</a></div>
<div class="product" style="left:384px"><div class="product-shot" role="img" aria-label="Hair shampoo bottle on purple backdrop"></div><div class="product-name">Hair Shampoo</div><div class="product-price">$50</div><a class="btn btn-ghost" style="position:relative;margin-top:16px;width:167px;height:40px">Add to Cart</a></div>
<div class="product" style="left:646px"><div class="product-shot" role="img" aria-label="Hair conditioner bottle on purple backdrop"></div><div class="product-name">Hair Conditioner</div><div class="product-price">$50</div><a class="btn btn-ghost" style="position:relative;margin-top:16px;width:167px;height:40px">Add to Cart</a></div>
<div class="product" style="left:909px"><div class="product-shot" role="img" aria-label="Hair shampoo bottle on purple backdrop"></div><div class="product-name">Hair Shampoo</div><div class="product-price">$50</div><a class="btn btn-ghost" style="position:relative;margin-top:16px;width:167px;height:40px">Add to Cart</a></div>

<h2 class="abs section-title" style="left:0;width:1200px;text-align:center;top:2222px;font-size:52px">GALLERY</h2>
<div class="abs" role="img" aria-label="Salon styling chairs facing framed mirrors" style="left:45px;top:2322px;width:320px;height:476px;background:linear-gradient(180deg,#f2f1ee 0%,#e6e4de 40%,#e2d8c4 75%,#cfc6b4 100%)"></div>
<div class="abs" role="img" aria-label="Wash basin room with lavender lighting" style="left:378px;top:2322px;width:438px;height:476px;background:linear-gradient(180deg,#f5f4f8 0%,#e9e6f3 30%,#c9b8ee 48%,#e4e0ee 62%,#f1f0f4 100%)"></div>
<div class="abs" role="img" aria-label="Retail shelves of hair care products" style="left:828px;top:2322px;width:325px;height:476px;background:linear-gradient(180deg,#ecebee 0%,#d9dde6 30%,#9fc4d6 52%,#dfe6ea 75%,#f1f0f1 100%)"></div>
<span class="dot" style="left:523px;background:var(--purple)"></span>
<span class="dot" style="left:577px"></span>
<span class="dot" style="left:631px"></span>

<section class="abs testimonial">
  <div class="abs" role="img" aria-label="Portrait photograph of the reviewing client" style="left:22px;top:39px;width:366px;height:345px;background:linear-gradient(90deg,#2fb6d9 0%,#6fc6dc 18%,#a0634a 40%,#c98f78 60%,#e4dad3 100%)"></div>
  <div class="abs" style="left:487px;top:62px;font-size:19px;font-weight:600">Maren Holt</div>
  <div class="abs" style="left:487px;top:92px;font-size:18px">Westmere, CA</div>
  <p class="abs serif" style="left:487px;top:130px;width:620px;font-size:29px;line-height:36px">“Lorem ipsum dolor sit amet, consectetur adipiscing elit, sed do eiusmod tempor incididunt ut labore et dolore magna aliqua. Quam viverra orci sagittis eu volutpat odio facilisis mauris sit”</p>
  <svg class="abs" style="left:1070px;top:340px" width="44" height="44" viewBox="0 0 44 44"><circle cx="22" cy="22" r="21" fill="#876aae"/><path d="M12 22h20M26 16l6 6-6 6" stroke="#fff" stroke-width="2" fill="none"/></svg>
</section>

<section class="abs gift">
  <p class="abs serif" style="left:103px;top:50px;width:580px;font-size:28px;line-height:37px">We offer you gift vouchers in selected value that are valid for any service from our offer. We take care of the rest.</p>
  <a class="btn btn-solid" style="left:103px;top:255px;width:249px;height:58px">Buy Gift Certificate</a>
  <div class="abs" role="img" aria-label="Salon interior with styling stations and lavender accent wall" style="left:708px;top:0;width:492px;height:396px;background:linear-gradient(90deg,#9f8fcf 0%,#c9c0e3 22%,#f3f2f2 45%,#ebe4d6 70%,#f4f3f1 100%)"></div>
</section>

<section class="abs find">
  <h2 class="abs serif" style="left:102px;top:58px;font-weight:400;font-size:48px;color:var(--purple)">Where to find us?</h2>
  <div class="row" style="top:143px"><svg width="10" height="14" viewBox="0 0 10 14"><path d="M5 0a5 5 0 0 0-5 5c0 4 5 9 5 9s5-5 5-9a5 5 0 0 0-5-5zm0 7a2 2 0 1 1 0-4 2 2 0 0 1 0 4z" fill="#fff"/></svg>2208 Calder Avenue, Westmere, CA</div>
  <div class="row" style="top:191px"><svg width="12" height="12" viewBox="0 0 12 12"><path d="M2 1l2 0 1 3-1.5 1a7 7 0 0 0 3.5 3.5L8 7l3 1v2a1 1 0 0 1-1 1A10 10 0 0 1 1 2a1 1 0 0 1 1-1z" fill="#fff"/></svg>555-014-3826
    <svg style="margin-left:14px" width="12" height="9" viewBox="0 0 12 9"><rect width="12" height="9" fill="#fff"/><path d="M0 0l6 5 6-5" stroke="#2b2d2b" fill="none"/></svg>hello@lumerasolenne.com</div>
  <div class="abs" style="left:102px;top:244px;font-size:10px">WORKING HOURS</div>
  <div class="abs" style="left:102px;top:258px;font-size:14px">Working days 8:00 - 20:00 &amp; Sundays 8:00 - 16:00</div>
  <a class="btn btn-solid" style="left:102px;top:328px;width:249px;height:58px">Book Appointment</a>
  <div class="abs" role="img" aria-label="Street map showing the salon location" style="left:732px;top:56px;width:365px;height:330px;background:linear-gradient(180deg,#ececec 0%,#e6e6e6 55%,#d8ead4 80%,#bfe3b9 100%)"></div>
</section>

<footer class="abs site-footer">
  <div class="abs" style="left:150px;top:37px;width:200px;text-align:center;font-size:13px">FOLLOW US</div>
  <div class="social"><span><i></i>Friendwall</span><span><i></i>Snapgram</span></div>
  <div class="abs" style="left:0;width:1200px;top:38px;text-align:center;font-size:26px;letter-spacing:1px">Velmora</div>
  <div class="abs" style="left:0;width:1200px;top:100px;text-align:center;font-size:14px">by Lumera Solenne</div>
  <div class="abs" style="left:850px;top:37px;width:176px;text-align:center;font-size:13px">DOWNLOAD OUR APP</div>
  <div class="app-badge" style="top:71px">Brindle App Market</div>
  <div class="app-badge" style="top:100px">Orchard Appshelf</div>
  <nav class="footer-nav"><span>ABOUT</span><span>SERVICES</span><span>SHOP</span><span>PHOTOS</span><span>CONTACT</span></nav>
  <div class="abs" style="left:0;width:1200px;top:204px;text-align:center;font-size:9px">Lumerasolenne 2021 © All rights reserved</div>
</footer>

</body>
</html>
```